Tidewell Grove Vitamin C Serum

We need a product label and box designed for our Vitamin C Serum product. The label will go on a 2oz bottle and the box will hold the 2oz bottle. Attached are the box and label templates as well as a Vitamin C Serum we have with another brand.

For this brand, we're looking to have the product look high end/luxury.

Target Market(s)

40+ year old women

```html
<!DOCTYPE html>
<html lang="en">
<head>
<meta charset="utf-8">
<title>Tidewell Grove Vitamin C Serum – Label and Box</title>
<link href="https://fonts.googleapis.com/css2?family=Montserrat:wght@400;500&family=Roboto+Condensed:wght@400&display=swap" rel="stylesheet">
<style>
  :root {
    --canvas: #e4e5e8;
    --paper: #ffffff;
    --ink: #3b3b3d;
    --orange: #ec6c2c;
    --orange-deep: #c63a1c;
    --orange-soft: #e7773a;
    --gold: #efb43a;
    --gold-deep: #e39a26;
    --side-text: #fff4ec;
  }
  * { box-sizing: border-box; margin: 0; padding: 0; }
  html, body { width: 1200px; height: 900px; overflow: hidden; }
  body {
    background: var(--canvas);
    font-family: "Montserrat", sans-serif;
    color: var(--ink);
    position: relative;
  }

  .brand {
    display: flex; flex-direction: column; align-items: center;
  }
  .brand-mark {
    border-radius: 50%;
    background: var(--orange);
  }
  .brand-name {
    font-family: "Montserrat", sans-serif;
    font-weight: 500;
    color: var(--ink);
    letter-spacing: 1px;
    text-transform: uppercase;
    white-space: nowrap;
  }

  .product-badge {
    background: var(--orange);
    color: var(--paper);
    font-family: "Montserrat", sans-serif;
    font-weight: 500;
    text-transform: uppercase;
    letter-spacing: 0.5px;
    white-space: nowrap;
    text-align: center;
  }

  /* Bottle label */
  .bottle-label {
    position: absolute;
    left: 90px; top: 190px;
    width: 390px; height: 520px;
    background: var(--paper);
    display: flex; flex-direction: column; align-items: center;
  }
  .bottle-label .brand { margin-top: 78px; }
  .bottle-label .brand-mark { width: 58px; height: 58px; margin-bottom: 46px; }
  .bottle-label .brand-name { font-size: 30px; }
  .bottle-label .product-badge {
    margin-top: 66px;
    font-size: 22px;
    padding: 13px 12px;
    width: 310px;
  }
  .volume-band {
    position: absolute; left: 0; right: 0; bottom: 40px;
    height: 48px;
    background: linear-gradient(180deg, var(--gold) 0%, var(--gold-deep) 100%);
    color: var(--paper);
    font-size: 15px;
    display: flex; align-items: center; justify-content: center;
  }

  /* Carton */
  .carton {
    position: absolute;
    left: 560px; top: 110px;
    display: flex;
    height: 680px;
  }
  .carton-front {
    width: 290px; height: 100%;
    background: var(--paper);
    position: relative;
    display: flex; flex-direction: column; align-items: center;
  }
  .carton-front .brand { margin-top: 230px; }
  .carton-front .brand-mark { width: 48px; height: 48px; margin-bottom: 34px; }
  .carton-front .brand-name { font-size: 24px; }
  .carton-front .product-badge {
    margin-top: 56px;
    font-size: 19px;
    padding: 11px 10px;
    width: 240px;
  }
  .carton-volume {
    position: absolute; bottom: 26px; left: 0; right: 0;
    text-align: center; font-size: 9px; color: var(--ink);
  }
  .carton-side {
    width: 260px; height: 100%;
    background: linear-gradient(180deg, var(--orange-deep) 0%, var(--orange-soft) 100%);
    color: var(--side-text);
    font-family: "Roboto Condensed", sans-serif;
    font-size: 12px;
    line-height: 1.45;
    padding: 250px 22px 0 20px;
  }
  .carton-side p { margin-bottom: 16px; }
  .carton-side .lot-note { margin-top: 70px; }
  .carton-side .version { margin-left: 14px; }
</style>
</head>
<body>

  <section class="bottle-label" aria-label="Bottle label">
    <div class="brand">
      <span class="brand-mark"></span>
      <h1 class="brand-name">Tidewell Grove</h1>
    </div>
    <p class="product-badge">Vitamin C Serum</p>
    <p class="volume-band">2 fl. oz (60ml)</p>
  </section>

  <section class="carton" aria-label="Carton panels">
    <div class="carton-front">
      <div class="brand">
        <span class="brand-mark"></span>
        <h2 class="brand-name">Tidewell Grove</h2>
      </div>
      <p class="product-badge">Vitamin C Serum</p>
      <p class="carton-volume">2 fl. oz (60ml)</p>
    </div>
    <div class="carton-side">
      <p>Directions:<br>
      Wash and pat skin dry. Apply small amount with fingertips to freshly cleansed and toned face, neck and decollete areas (avoid direct contact with eyes). Allow time to absorb prior to moisturizer application.</p>
      <p>For External use only. Discontinue use if redness or irritation occurs. Avoid direct contact with eyes. Keep out of reach of children. Do not use if seal is damaged or missing. Store in a cool, dark place.</p>
      <p class="lot-note">Lot no. and expiration date printed<br>on bottom of bottle<span class="version">V4R0</span></p>
    </div>
  </section>

</body>
</html>
```